Trucking & Excavation company needs ad designed

We need a general marketing ad designed that we can use for events and local publications. A past brochure is posted for some text info. I will also be eventually looking to design a brochure as well so this should somewhat be a shortened version of that. Looking to have an ad created that is 1/4 page and 1/2 page of standard 8 1/2 x 11.

Target Market(s)

Other Construction Companies looking for trucking and excavation needs

Industry/Entity Type

Trucking and Excavation

Font styles to use
Sans Serif

Colors
FFF300
FFF600
FEFA6F
FFFEC7
FFFEE8
EB3D1F
EC4F4E
F09395
F8D3D4
FCEDEE

Requirements
Must have
• This can be reworded but ultimately.... VANTRO Works, LLC. Has been servicing North Eastern Wisconsin since 1994 offering customers a one stop shop for all their trucking and excavation needs. Whether you need a load of gravel or hauling of debris from a large demolition project we will get it done. Commercial, Agricultural & Residential Excavation services for site preparation, basements, parking lots and demolition.
Nice to have
• Like to have our pictures not stock photos. The back of the business card bullets most of our services offered something like this would be great included

```html
<!DOCTYPE html>
<html lang="en">
<head>
<meta charset="utf-8">
<title>VANTRO Works, LLC – Trucking &amp; Excavation Ad</title>
<link rel="stylesheet" href="https://fonts.googleapis.com/css2?family=Lilita+One&family=Montserrat:wght@600;700;800&family=Source+Sans+3:wght@400;600;700&family=Oswald:wght@500&display=swap">
<style>
  :root{
    --green:#55b65c;
    --red:#e8262b;
    --yellow:#f3c41f;
    --ink:#222;
    --white:#fff;
    --page:#eeeeee;
  }
  *{box-sizing:border-box;margin:0;padding:0}
  html,body{width:750px;height:1200px;overflow:hidden;background:var(--page)}
  .ad{position:absolute;left:20px;top:350px;width:710px;height:500px;background:var(--white);overflow:hidden;box-shadow:0 4px 14px rgba(0,0,0,.12);font-family:"Source Sans 3",sans-serif}
  .ad > *{position:absolute}
  .hero-photo{left:0;top:0;width:710px;height:340px;
    clip-path:polygon(0 0,710px 0,710px 257px,382px 339px,0 257px);
    background:linear-gradient(180deg,#ffffff 0%,#f4f7f9 18%,#c9d6de 38%,#8fa2a9 55%,#a9b0b3 70%,#8c9296 100%)}
  .hero-fade{left:0;top:0;width:710px;height:130px;background:linear-gradient(180deg,rgba(255,255,255,.95) 60%,rgba(255,255,255,0))}
  .chevron{left:0;top:250px}
  .title{left:0;width:710px;top:12px;text-align:center;font-family:"Lilita One",sans-serif;font-size:48px;line-height:54px;color:var(--green);letter-spacing:1px}
  .rule{left:61px;width:589px;height:2px;background:var(--yellow)}
  .rule.top{top:70px}
  .rule.bottom{top:124px}
  .tagline{left:0;width:710px;top:78px;text-align:center;font-family:"Montserrat",sans-serif;font-weight:700;font-size:15.5px;line-height:20px;letter-spacing:.4px}
  .tagline .accent{color:var(--red)}
  .tagline .dark{color:var(--ink)}
  .services{left:27px;top:333px;width:260px}
  .services-label{font-family:"Montserrat",sans-serif;font-weight:600;font-size:11.5px;color:var(--green)}
  .services-head{font-family:"Montserrat",sans-serif;font-weight:800;font-size:16.5px;color:var(--red);line-height:20px;margin-top:2px}
  .services-sub{font-family:"Montserrat",sans-serif;font-weight:700;font-size:10.2px;color:var(--ink);margin-top:1px}
  .service-list{list-style:none;display:grid;grid-template-columns:146px 120px;row-gap:5px;margin-top:9px}
  .service-list li{display:flex;align-items:center;gap:6px;font-size:14px;color:var(--ink)}
  .brand{left:290px;top:386px;width:160px;text-align:center;font-family:"Lilita One",sans-serif;font-size:22px;line-height:26px;color:var(--green);display:flex;align-items:center;justify-content:center;gap:5px;white-space:nowrap}
  .brand-dot{flex:none;width:8px;height:8px;border-radius:50%;background:var(--red)}
  .pitch{right:31px;top:330px;text-align:right;color:var(--ink)}
  .pitch-region{font-family:"Montserrat",sans-serif;font-weight:700;font-size:12.5px}
  .pitch-line{display:flex;justify-content:flex-end;align-items:center;gap:6px;margin-top:2px}
  .since{background:var(--green);color:var(--white);font-family:"Oswald",sans-serif;font-size:9px;letter-spacing:2px;padding:1px 8px;height:13px;line-height:11px}
  .pitch-big{font-family:"Montserrat",sans-serif;font-weight:800;font-size:22px;line-height:23px}
  .pitch-big.red{color:var(--red)}
  .pitch-big.green{color:var(--green)}
  .pitch-shop{font-family:"Source Sans 3",sans-serif;font-weight:400;font-size:21px;line-height:22px;color:var(--red)}
  .pitch-needs{font-family:"Source Sans 3",sans-serif;font-weight:700;font-size:9.4px;margin-top:2px}
  .pitch-note{font-size:8.6px;line-height:11px}
  .pitch-note b{font-weight:700}
  .footer{left:0;top:0}
  .contact-label{left:27px;top:464px;font-family:"Oswald",sans-serif;font-weight:500;font-size:21px;color:var(--white);transform:scaleX(.85);transform-origin:left}
  .contact-items{left:127px;top:454px;font-size:11px;line-height:17px;color:var(--white)}
  .contact-items div{display:flex;align-items:center;gap:5px}
  .address{right:31px;top:471px;font-size:11px;color:var(--white)}
</style>
</head>
<body>
<main class="ad">
  <div class="hero-photo" role="img" aria-label="Photo of a red roll-off dumpster truck on an open road with hazy mountains behind"></div>
  <div class="hero-fade"></div>
  <svg class="chevron" width="710" height="100" viewBox="0 250 710 100" aria-hidden="true">
    <polygon points="0,257 382,339 710,257 710,266 382,346 0,266" fill="#55b65c"/>
  </svg>

  <h1 class="title">VANTRO WORKS, LLC</h1>
  <div class="rule top"></div>
  <p class="tagline"><span class="accent">NEED A LOAD A GRAVEL OR HAULING OF DEBRIS FROM A LARGE</span><br><span class="dark">DEMOLITION PROJECT VANTRO WORKS LLC IS BEST FOR YOU</span></p>
  <div class="rule bottom"></div>

  <section class="services">
    <div class="services-label">OUR SERVICES</div>
    <div class="services-head">COMMERCIAL &amp; RESIDENTIAL</div>
    <div class="services-sub">AGRICULTURAL &amp; RESIDENTIAL EXCAVATION</div>
    <ul class="service-list">
      <li><svg width="11" height="11" viewBox="0 0 12 12"><circle cx="6" cy="6" r="6" fill="#55b65c"/><path d="M3.2 6.2l1.9 1.9 3.7-3.8" stroke="#fff" stroke-width="1.6" fill="none"/></svg>Site Preparation</li>
      <li><svg width="11" height="11" viewBox="0 0 12 12"><circle cx="6" cy="6" r="6" fill="#55b65c"/><path d="M3.2 6.2l1.9 1.9 3.7-3.8" stroke="#fff" stroke-width="1.6" fill="none"/></svg>Basements</li>
      <li><svg width="11" height="11" viewBox="0 0 12 12"><circle cx="6" cy="6" r="6" fill="#55b65c"/><path d="M3.2 6.2l1.9 1.9 3.7-3.8" stroke="#fff" stroke-width="1.6" fill="none"/></svg>Parking Lots</li>
      <li><svg width="11" height="11" viewBox="0 0 12 12"><circle cx="6" cy="6" r="6" fill="#55b65c"/><path d="M3.2 6.2l1.9 1.9 3.7-3.8" stroke="#fff" stroke-width="1.6" fill="none"/></svg>Demolition</li>
    </ul>
  </section>

  <div class="brand"><span class="brand-name">VANTRO Works</span><span class="brand-dot"></span></div>

  <section class="pitch">
    <div class="pitch-region">NORTH EASTERN WISCONSIN</div>
    <div class="pitch-line"><span class="since">SINCE 1994</span><span class="pitch-big red">OFFERING</span></div>
    <div class="pitch-big green">FOR CUSTOMERS</div>
    <div class="pitch-shop">A ONE STOP SHOP</div>
    <div class="pitch-needs">FOR ALL THEIR TRUCKING &amp; EXCAVATION NEEDS</div>
    <div class="pitch-note">We primarily operate in <b>North Eastern Wisconsin –</b><br>from Brown County and ad joining counties.</div>
  </section>

  <svg class="footer" width="710" height="500" viewBox="0 0 710 500" aria-hidden="true">
    <polygon points="0,450 316,450 370,500 0,500" fill="#f3c41f"/>
    <polygon points="342,467 710,467 710,500 375,500" fill="#55b65c"/>
  </svg>
  <div class="contact-label">CONTACT US:</div>
  <div class="contact-items">
    <div><svg width="9" height="7" viewBox="0 0 9 7"><rect width="9" height="7" fill="#222"/><path d="M0 0l4.5 3.6L9 0" stroke="#f3c41f" stroke-width="1" fill="none"/></svg>hello@vantroworks.com</div>
    <div><svg width="9" height="9" viewBox="0 0 10 10"><circle cx="5" cy="5" r="4.3" fill="none" stroke="#222" stroke-width="1"/><ellipse cx="5" cy="5" rx="1.9" ry="4.3" fill="none" stroke="#222" stroke-width="1"/><path d="M.7 5h8.6" stroke="#222" stroke-width="1"/></svg>vantroworks.com</div>
  </div>
  <div class="address">VANTRO Works LLC 1450 Birchline Road&nbsp; Ashford, WI 54000</div>
</main>
</body>
</html>
```